Graphic to communicate emotional connection

Howdy-I need a graphic that describe my financial planning process.The attached is a concept, but please use your own creativity to show how you would display this:- The four circles on the outside (Protect what we have, know where it goes, make it grow, and dignity and independence) are the four major areas of concern- Then, there are three value statements:- The first is the most powerful which is that Clarity leads to Control which allows your Intentions to come through- The second shows that we take our clients from Uncertainty and Confusion, to Confidence and Intention- The third says we create space for you to develop your Purposeful Effort which leads to Your Best Financial Life.I've also attached my logo - please use the colors in my logo and maybe add a soft green as needed.The reader should be able to briefly scan this document and understand that we will connect with them on an emotional level to get their finances in shape.Thanks!-Tam

Target Market(s)

wealthy women, whether independent or married

Industry/Entity Type

Financial Planning

Requirements
Must have
• Please use the colors in my logo plus a soft green as needed
Should not have
• This should not be a busy or hard-to-read graphic. It is meant to convey an that I try to make an emotional connection, at a glance.

```html
<!DOCTYPE html>
<html lang="en">
<head>
<meta charset="utf-8">
<title>Our Aspiration – Harbor Lane Wealth</title>
<link rel="stylesheet" href="https://fonts.googleapis.com/css2?family=Tinos:wght@400;700&display=swap">
<style>
  :root {
    --navy: #0f2f78;
    --navy-deep: #0b2666;
    --ring: #eef1f6;
    --soft-green: #d9ebd2;
    --arrow: #a9b8d4;
    --white: #ffffff;
  }
  html, body {
    margin: 0;
    padding: 0;
    width: 1052px;
    height: 1200px;
    overflow: hidden;
    background: var(--white);
  }
  .canvas {
    position: relative;
    width: 1052px;
    height: 1200px;
    font-family: "Tinos", "Times New Roman", serif;
    color: var(--navy);
  }
  .ring-area {
    position: absolute;
    left: 91px;
    top: 202px;
    width: 882px;
    height: 794px;
    box-sizing: border-box;
    border: 106px solid var(--ring);
    border-radius: 50%;
  }
  .brand {
    position: absolute;
    top: 284px;
    left: 0;
    width: 1052px;
    display: flex;
    justify-content: center;
    align-items: center;
    gap: 10px;
  }
  .brand-mark {
    width: 30px;
    height: 30px;
    background: var(--navy);
  }
  .brand-name {
    font-size: 22px;
    letter-spacing: 1px;
    color: var(--navy);
  }
  .title {
    position: absolute;
    top: 370px;
    left: 0;
    width: 1052px;
    margin: 0;
    text-align: center;
    font-size: 39px;
    font-weight: 400;
    letter-spacing: 7px;
  }
  .value-band {
    position: absolute;
    left: 278px;
    top: 457px;
    width: 495px;
    height: 44px;
    background: var(--soft-green);
    display: flex;
    align-items: center;
    justify-content: center;
    gap: 12px;
    font-size: 24px;
  }
  .value-band svg { width: 30px; height: 26px; }
  .concern {
    position: absolute;
    width: 168px;
    height: 111px;
    border-radius: 56px;
    background: linear-gradient(160deg, #1a3d8c 0%, var(--navy) 35%, var(--navy-deep) 100%);
    box-shadow: 6px 8px 14px rgba(0, 0, 0, 0.18);
    color: var(--white);
    display: flex;
    align-items: center;
    justify-content: center;
    text-align: center;
    font-size: 19px;
    line-height: 1.2;
  }
  .concern--protect { left: 71px; top: 415px; }
  .concern--know { left: 813px; top: 415px; }
  .concern--grow { left: 71px; top: 714px; }
  .concern--dignity { left: 818px; top: 714px; font-size: 17.5px; }

  .step { position: absolute; width: 178px; }
  .step-tab {
    margin: 0 auto;
    width: 129px;
    height: 26px;
    border-radius: 12px 12px 0 0;
    background: var(--navy);
    color: var(--white);
    font-size: 10.5px;
    line-height: 1.15;
    display: flex;
    align-items: center;
    justify-content: center;
    text-align: center;
  }
  .step-card {
    height: 53px;
    border-radius: 27px;
    background: var(--white);
    box-shadow: 4px 6px 10px rgba(0, 0, 0, 0.2);
    display: flex;
    align-items: center;
    justify-content: center;
    text-align: center;
    font-size: 15px;
    line-height: 1.2;
    margin-top: -2px;
    position: relative;
  }
  .step--from { left: 273px; top: 560px; }
  .step--to { left: 603px; top: 560px; }
  .step--effort { left: 273px; top: 665px; }
  .step--life { left: 603px; top: 665px; }

  .flow-arrow {
    position: absolute;
    left: 507px;
    width: 52px;
    height: 45px;
  }
  .flow-arrow--first { top: 591px; }
  .flow-arrow--second { top: 696px; }
</style>
</head>
<body>
<main class="canvas">
  <div class="ring-area" role="img" aria-label="Soft decorative ring of pale segments around the centre"></div>

  <header class="brand">
    <span class="brand-mark"></span>
    <span class="brand-name">HARBOR LANE WEALTH</span>
  </header>

  <h1 class="title">OUR ASPIRATION</h1>

  <div class="value-band">
    <span>CLARITY</span>
    <svg viewBox="0 0 30 26" aria-hidden="true"><path d="M0 8h16V0l14 13-14 13v-8H0z" fill="#fff"/></svg>
    <span>CONTROL</span>
    <svg viewBox="0 0 30 26" aria-hidden="true"><path d="M0 8h16V0l14 13-14 13v-8H0z" fill="#fff"/></svg>
    <span>INTENTION</span>
  </div>

  <div class="concern concern--protect">PROTECT<br>WHAT WE<br>HAVE</div>
  <div class="concern concern--know">KNOW<br>WHERE IT<br>GOES</div>
  <div class="concern concern--grow">MAKE IT<br>GROW</div>
  <div class="concern concern--dignity">DIGNITY AND<br>INDEPENDENCE</div>

  <div class="step step--from">
    <div class="step-tab">WE TAKE YOU FROM</div>
    <div class="step-card">UNCERTAINTY<br>CONFUSION</div>
  </div>
  <svg class="flow-arrow flow-arrow--first" viewBox="0 0 52 45" aria-hidden="true">
    <path d="M0 13h26V0l26 22.5L26 45V32H0z" fill="var(--arrow)"/>
  </svg>
  <div class="step step--to">
    <div class="step-tab">TO</div>
    <div class="step-card">CONFIDENCE<br>INTENTION</div>
  </div>

  <div class="step step--effort">
    <div class="step-tab">WE CREATE SPACE<br>FOR YOUR</div>
    <div class="step-card">PURPOSEFUL<br>EFFORT</div>
  </div>
  <svg class="flow-arrow flow-arrow--second" viewBox="0 0 52 45" aria-hidden="true">
    <path d="M0 13h26V0l26 22.5L26 45V32H0z" fill="var(--arrow)"/>
  </svg>
  <div class="step step--life">
    <div class="step-tab">WHICH LEADS TO</div>
    <div class="step-card">YOUR BEST<br>FINANCIAL LIFE</div>
  </div>
</main>
</body>
</html>
```